Online Prescription Eyeglass Lens Company Needs a Website

*Update new name to Glintwell. Thx

We are eye doctors with a lab that need a website for a new company based in Southern California called Glintwell. We replace old prescription lenses with new ones next day for most lenses. Patients select the lenses and give us the prescription. We then send a box with a prepaid shipping label. Place the frames in the box and drop them in the mail to our lab. We will custom make new lenses, fit them back into your frames and send them back to you. We would like to compete with www.spectrafold.com and offer affordable lenses for single vision, bifocal, progressive, sunglass lenses at an affordable price with next day shipping.
Updates

Hi Designers, We have a new name called Glintwell. Can we have the website design reflect the new name and we'll pick our favorites. Thx

Update: The new name is Brightmoor . I have not made very many changes or feedback to the submissions because we were bidding for a .com. We won and our new name is Brightmoor . This is the last name change.. Please have the website reflect the new name and I'll be providing feedback on the websites . ( I have a separate project for the logo people are working on, so don't worry about creating a logo). Look forward to the submissions. Thanks everyone.

Hi, Just leave the name as Glintwell for now. I will narrow down top designs tonight. Thx

Target Market(s)

Anyone that wears prescription or nonprescription glasses or sunglasses that want next day shipping.

Industry/Entity Type

Eyewear

Number of Pages Required

4 page

Font styles to use
Serif

Colors

Designer to choose colors to be used in the design.

Requirements
Must have
• I need a website that can compete with https://www.spectrafold.com/.
• We are different from spectrafold because we can offer same day service or next day shipping.
• It needs to have website that offers the lenses available listed below.
• Needs to be able to upload a prescription and payment feature.
• Pictures of different types of options with small info about each lens option.
• Template Pricing (just use numbers from $79-$179 for now)
• SINGLE VISION LENSES
• HIGH INDEX LENSES
• READING LENSES
• DIGITAL HD PROGRESSIVE LENSES
• RX & NON-RX SUNGLASSES
• RX & NON-RX POLARIZED SUNGLASSES
• COMPUTER LENSES
• TRANSITION LENSES
• BI-FOCAL LENSES

```html
<!DOCTYPE html>
<html lang="en">
<head>
<meta charset="utf-8">
<title>Glintwell — Prescription Lenses</title>
<link href="https://fonts.googleapis.com/css2?family=Bitter:wght@400;500;600&family=Jost:wght@400;500&display=swap" rel="stylesheet">
<style>
:root{
  --blue:#1aa3e0;
  --blue-dark:#0e7a9a;
  --navy:#1d2a3f;
  --ink:#2b2b2b;
  --muted:#6b6b6b;
  --pale:#dcf0fa;
  --footer:#1b1d20;
  --white:#ffffff;
}
*{box-sizing:border-box;margin:0;padding:0}
html,body{width:1200px;height:3364px;overflow:hidden}
body{position:relative;font-family:'Jost',sans-serif;color:var(--ink);background:var(--white)}
.abs{position:absolute}
.serif{font-family:'Bitter',serif}
.btn{position:absolute;display:flex;align-items:center;justify-content:center;border-radius:30px;color:var(--white);font-size:13px}
.btn-blue{background:var(--blue)}
.section-title{position:absolute;left:0;width:1200px;text-align:center;font-family:'Bitter',serif;font-size:30px;font-weight:500;color:var(--ink)}
.section-title span{color:var(--blue)}
.rule{position:absolute;left:575px;width:50px;height:2px;background:#bbb}

/* top bar */
.topbar{left:0;top:0;width:1200px;height:40px;background:var(--blue);color:var(--white);font-size:14px}
.topbar .phone{left:140px;top:8px;display:flex;align-items:center;gap:10px}
.topbar .account{left:965px;top:11px;font-size:13px}

/* nav */
.logo{font-family:'Bitter',serif;font-size:30px;font-weight:500;color:var(--ink)}
.nav a{position:absolute;top:72px;font-size:13px;color:var(--ink);text-decoration:none}
.nav a.active{color:var(--blue);text-decoration:underline}
.cart{left:930px;top:58px;display:flex;gap:10px;align-items:center}
.cart-icon{width:40px;height:40px;border-radius:50%;background:var(--blue);display:flex;align-items:center;justify-content:center}
.cart-text{font-size:12px;line-height:1.2}
.cart-text b{color:var(--blue);font-weight:500;font-size:15px}

/* hero */
.hero{left:0;top:123px;width:1200px;height:485px;background:linear-gradient(90deg,#cfd1d3 0%,#a6a8aa 45%,#3a3a3c 70%,#6f7072 100%)}
.hero-title{left:172px;top:267px;color:var(--white);font-size:38px}
.hero-sub{left:172px;top:323px;color:var(--white);font-size:22px}
.shop{left:172px;top:380px;width:160px;height:46px;background:#222;font-size:17px}
.dots{left:172px;top:460px;display:flex;gap:5px}
.dots i{width:12px;height:12px;border-radius:50%;border:2px solid var(--white)}
.dots i:first-child{background:var(--white)}

/* about */
.about-text{left:143px;top:735px;width:914px;text-align:center;font-size:12.5px;line-height:22px;color:var(--muted)}

/* products */
.products{left:0;top:935px;width:1200px;height:904px;background-color:var(--pale);background-image:radial-gradient(#b9dff2 1.5px,transparent 1.6px);background-size:22px 22px}
.card{position:absolute;width:206px;height:229px;background:var(--blue-dark);border-radius:4px;text-align:center;color:var(--white)}
.card.featured{background:var(--blue)}
.card .thumb{position:absolute;left:33px;top:-61px;width:140px;height:140px;border-radius:50%;border:5px solid var(--white);background:linear-gradient(135deg,#dfe6ea,#9fb3bd)}
.card h3{position:absolute;top:100px;left:0;width:100%;font-family:'Bitter',serif;font-weight:400;font-size:16px;line-height:20px}
.card .price{position:absolute;top:146px;left:0;width:100%;font-size:15px}
.card .add{position:absolute;left:38px;top:175px;width:130px;height:28px;border-radius:16px;background:#1f2326;font-size:12px;display:flex;align-items:center;justify-content:center;gap:8px}

/* different */
.feature{position:absolute;text-align:center;font-size:20px;color:var(--ink)}
.or{left:574px;top:2009px;width:42px;height:42px;border-radius:50%;background:#1f2326;color:var(--white);display:flex;align-items:center;justify-content:center;font-family:'Bitter',serif;font-size:15px}

/* our lenses */
.lenses{left:0;top:2176px;width:1200px;height:365px;background:linear-gradient(90deg,#8d9aa6,#aab5be 55%,#c7cfd5)}
.lenses-photo{left:670px;top:2176px;width:530px;height:365px;background:linear-gradient(90deg,rgba(199,207,213,0),#3a3d44 40%,#2c2f35 70%,#b9c2c9)}
.lenses h2{}
.lenses-text{left:143px;top:2284px;width:600px;font-size:14.5px;line-height:20px;color:var(--white)}

/* reviews */
.review{position:absolute;width:467px;height:148px;background:var(--white);box-shadow:0 2px 10px rgba(0,0,0,.12);padding:28px 30px;font-size:12.5px;line-height:20px;color:#333}
.quote{position:absolute;right:28px;bottom:14px;font-family:'Bitter',serif;font-size:70px;line-height:50px;color:#e2e2e2}
.avatar{position:absolute;width:86px;height:86px;border-radius:50%;border:3px solid var(--blue);background:linear-gradient(135deg,#d8c8b8,#8c7a6a)}
.reviewer{position:absolute;font-size:16px;color:#333}
.stars{position:absolute;color:var(--blue);font-size:14px;letter-spacing:2px}

/* newsletter */
.newsletter{left:0;top:3001px;width:1200px;height:54px;background:var(--blue)}
.nl-title{left:195px;top:3014px;color:var(--white);font-size:20px}
.nl-input{left:478px;top:3012px;width:462px;height:32px;background:var(--white);font-size:11px;color:#aaa;padding:9px 14px;font-style:italic}
.nl-btn{left:940px;top:3012px;width:119px;height:32px;background:var(--navy);color:var(--white);font-size:14px;display:flex;align-items:center;justify-content:center}

/* footer */
.footer{left:0;top:3055px;width:1200px;height:309px;background:linear-gradient(180deg,#2a2c30,var(--footer))}
.f-head{position:absolute;top:3094px;color:var(--white);font-size:15px}
.f-links{left:148px;top:3130px;list-style:none;color:#ddd;font-size:12px;line-height:26px}
.f-links li::before{content:"›";color:var(--blue);margin-right:8px}
.f-contact{left:348px;top:3132px;color:#ddd;font-size:12px;line-height:16px}
.f-contact div{display:flex;gap:10px;margin-bottom:12px}
.f-field{position:absolute;left:597px;width:188px;height:26px;background:var(--white);font-size:10px;font-style:italic;color:#999;padding:6px 8px}
.f-submit{left:597px;top:3246px;width:70px;height:26px;background:var(--blue);border-radius:14px;color:var(--white);font-size:11px;display:flex;align-items:center;justify-content:center}
.f-logo{left:886px;top:3160px;color:var(--white);font-size:34px}
.social{position:absolute;top:3229px;width:22px;height:22px;border-radius:50%;background:var(--blue)}
.f-line{left:143px;top:3320px;width:916px;height:1px;background:#3d4045}
.copy{left:0;top:3330px;width:1200px;text-align:center;color:#bbb;font-size:12px}
</style>
</head>
<body>

<!-- top bar -->
<div class="abs topbar">
  <div class="abs phone">
    <svg width="24" height="24" viewBox="0 0 24 24"><circle cx="12" cy="12" r="11" fill="none" stroke="#fff" stroke-width="1.6"/><path d="M8.5 7.2l1.6-.4 1.1 2.4-1 .9c.5 1.3 1.4 2.2 2.7 2.8l.9-1 2.4 1.1-.4 1.6c-4 .3-7.6-3.4-7.3-7.4z" fill="#fff"/></svg>
    <span>123-456-7890</span>
  </div>
  <div class="abs account">Login &nbsp;|&nbsp; Register</div>
</div>

<!-- header -->
<div class="abs logo" style="left:143px;top:60px">Glintwell</div>
<nav class="nav">
  <a class="active" href="#" style="left:477px">Home</a>
  <a href="#" style="left:551px">About Us</a>
  <a href="#" style="left:651px">Products</a>
  <a href="#" style="left:747px">FAQ's</a>
  <a href="#" style="left:826px">Contact Us</a>
</nav>
<div class="abs cart">
  <div class="cart-icon"><svg width="20" height="18" viewBox="0 0 20 18"><path d="M1 2h3l2.5 10h10L19 5H5.5" fill="none" stroke="#fff" stroke-width="1.8"/><circle cx="8" cy="15.5" r="1.5" fill="#fff"/><circle cx="15" cy="15.5" r="1.5" fill="#fff"/></svg></div>
  <div class="cart-text">Cart: 0 Items<br><b>$0.00</b></div>
</div>

<!-- hero -->
<div class="abs hero" role="img" aria-label="Photo of a stylish couple wearing eyeglasses in a city setting"></div>
<svg class="abs" style="left:0;top:0" width="1200" height="620"><polygon points="143,206 683,206 143,600" fill="var(--blue)"/></svg>
<h1 class="abs hero-title serif" style="font-weight:400">Complete Eyeglasses</h1>
<div class="abs hero-sub">Starting At $79-$179</div>
<div class="btn shop">Shop Now</div>
<div class="abs dots"><i></i><i></i><i></i></div>

<!-- about -->
<h2 class="section-title" style="top:662px">About <span>Glintwell</span></h2>
<div class="rule" style="top:710px"></div>
<p class="abs about-text">Lorem ipsum dolor sit amet, consectetuer adipiscing elit, sed diam nonummy nibh euismod tincidunt ut laoreet dolore magna aliquam erat volutpat. Ut wisi enim ad minim veniam, quis nostrud exerci tation ullamcorper suscipit lobortis nisl ut aliquip ex ea commodo consequat. Duis autem vel eum iriure dolor in hendrerit in vulputate velit esse molestie consequat, vel illum dolore eu feugiat nulla facilisis at vero eros et accumsan et iusto odio dignissim qui blandit praesent luptatum zzril delenit augue duis dolore te feugait nulla facilisi euismod tincidunt ut laoreet dolore magna aliquam erat.</p>
<div class="btn btn-blue" style="left:545px;top:840px;width:110px;height:30px">Read More</div>

<!-- products -->
<section class="abs products"></section>
<h2 class="section-title" style="top:990px">Our <span>Products</span></h2>

<div class="card featured" style="left:143px;top:1144px"><div class="thumb" role="img" aria-label="Desk with eyeglasses and books"></div><h3>Single Vision<br>Lenses</h3><div class="price">$78.00</div><div class="add">🛒 Add to cart</div></div>
<div class="card" style="left:379px;top:1144px"><div class="thumb" role="img" aria-label="Woman wearing glasses"></div><h3>High Index<br>Lenses</h3><div class="price">$120.00</div><div class="add">🛒 Add to cart</div></div>
<div class="card" style="left:617px;top:1144px"><div class="thumb" role="img" aria-label="Reading glasses in front of an eye chart"></div><h3>Reading<br>Lenses</h3><div class="price">$92.00</div><div class="add">🛒 Add to cart</div></div>
<div class="card" style="left:852px;top:1144px"><div class="thumb" role="img" aria-label="Bright modern room"></div><h3>Digital Hd<br>Progressive Lenses</h3><div class="price">$135.00</div><div class="add">🛒 Add to cart</div></div>

<div class="card" style="left:143px;top:1480px"><div class="thumb" role="img" aria-label="Man wearing glasses"></div><h3>Rx &amp; Non-Rx<br>Sunglasses</h3><div class="price">$142.00</div><div class="add">🛒 Add to cart</div></div>
<div class="card" style="left:379px;top:1480px"><div class="thumb" role="img" aria-label="Pair of black frame glasses"></div><h3>Rx &amp; Non-rx Polarized<br>Sunglasses</h3><div class="price">$84.00</div><div class="add">🛒 Add to cart</div></div>
<div class="card" style="left:617px;top:1480px"><div class="thumb" role="img" aria-label="Glasses resting on a keyboard"></div><h3>Computer<br>Lenses</h3><div class="price">$124.00</div><div class="add">🛒 Add to cart</div></div>
<div class="card" style="left:852px;top:1480px"><div class="thumb" role="img" aria-label="Man wearing transition lenses"></div><h3>Transition<br>Lenses</h3><div class="price">$111.00</div><div class="add">🛒 Add to cart</div></div>

<div class="btn btn-blue" style="left:547px;top:1746px;width:106px;height:30px">View All</div>

<!-- different -->
<h2 class="section-title" style="top:1897px;font-size:25px">We Are Different From Spectrafold Because We Can Offer</h2>
<svg class="abs" style="left:385px;top:1960px" width="120" height="120" viewBox="0 0 120 120">
  <text x="28" y="22" font-family="Bitter,serif" font-size="19" fill="var(--blue)">Same</text>
  <text x="8" y="40" font-family="Bitter,serif" font-size="19" fill="var(--blue)">Day</text>
  <path d="M30 60 A38 38 0 1 0 60 34" fill="none" stroke="var(--blue)" stroke-width="7"/>
  <polygon points="22,54 38,54 30,68" fill="var(--blue)"/>
  <path d="M70 52v24h18" fill="none" stroke="var(--blue)" stroke-width="6"/>
</svg>
<div class="feature" style="left:340px;top:2090px;width:200px">Same Day Service</div>
<div class="abs or">Or</div>
<svg class="abs" style="left:700px;top:1985px" width="130" height="80" viewBox="0 0 130 80">
  <g fill="var(--blue)">
    <rect x="0" y="10" width="30" height="6"/><rect x="8" y="24" width="26" height="6"/><rect x="0" y="38" width="30" height="6"/><rect x="12" y="52" width="22" height="6"/>
    <rect x="38" y="6" width="56" height="50"/>
    <path d="M98 20h16l14 18v18h-30z"/>
    <circle cx="58" cy="64" r="9"/><circle cx="112" cy="64" r="9"/>
  </g>
  <circle cx="58" cy="64" r="4" fill="#fff"/><circle cx="112" cy="64" r="4" fill="#fff"/>
  <path d="M104 26h8l9 12h-17z" fill="#fff"/>
</svg>
<div class="feature" style="left:656px;top:2090px;width:200px">Next Day Shipping</div>

<!-- our lenses -->
<section class="abs lenses"></section>
<div class="abs lenses-photo" role="img" aria-label="Smiling couple wearing eyeglasses"></div>
<h2 class="abs serif" style="left:143px;top:2236px;font-size:28px;font-weight:400;color:#fff">Our Lenses</h2>
<p class="abs lenses-text">Lorem ipsum dolor sit amet, consectetuer adipiscing elit, sed diam nonummy nibh euismod tincidunt ut laoreet dolore magna aliquam erat volutpat. Ut wisi enim ad minim veniam, quis nostrud exerci tation ullamcorper suscipit lobortis nisl ut aliquip ex ea commodo consequat.</p>
<div class="abs" style="left:143px;top:2390px;color:#fff;font-size:14.5px">our lenses Prices starts from $79-$179</div>
<div class="btn btn-blue" style="left:143px;top:2438px;width:187px;height:32px">Learn About Our Lenses</div>

<!-- reviews -->
<h2 class="section-title" style="top:2597px;font-size:28px">Customer <span>Reviews</span></h2>
<svg class="abs" style="left:74px;top:2752px" width="30" height="60"><path d="M26 2L4 30l22 28" fill="none" stroke="#ccc" stroke-width="2"/></svg>
<svg class="abs" style="left:1096px;top:2752px" width="30" height="60"><path d="M4 2l22 28L4 58" fill="none" stroke="#ccc" stroke-width="2"/></svg>

<div class="review" style="left:143px;top:2689px">Lorem ipsum dolor sit amet, consectetuer adipiscing elit, sed diam nonummy nibh euismod tincidunt ut laoreet dolore magna aliquam erat volutpat. Ut wisi enim ad minim veniam, quis nostrud exerci tation ullamcorper suscipit lobortis nisl ut aliquip ex ea.<span class="quote">”</span></div>
<div class="avatar" style="left:164px;top:2822px" role="img" aria-label="Customer portrait"></div>
<div class="reviewer" style="left:263px;top:2848px">Lorem ipsum dolor</div>
<div class="stars" style="left:263px;top:2872px">★★★★★</div>

<div class="review" style="left:592px;top:2721px">Lorem ipsum dolor sit amet, consectetuer adipiscing elit, sed diam nonummy nibh euismod tincidunt ut laoreet dolore magna aliquam erat volutpat. Ut wisi enim ad minim veniam, quis nostrud exerci tation ullamcorper suscipit lobortis nisl ut aliquip ex ea.<span class="quote">”</span></div>
<div class="avatar" style="left:612px;top:2853px" role="img" aria-label="Customer portrait"></div>
<div class="reviewer" style="left:712px;top:2878px">Lorem ipsum dolor</div>
<div class="stars" style="left:712px;top:2902px">★★★★★</div>

<!-- newsletter -->
<section class="abs newsletter"></section>
<svg class="abs" style="left:143px;top:3008px" width="40" height="40" viewBox="0 0 40 40"><rect x="3" y="12" width="34" height="24" fill="#f08a24"/><path d="M3 12l17 13 17-13" fill="none" stroke="#fff" stroke-width="2"/><rect x="10" y="4" width="20" height="14" fill="#fff"/></svg>
<div class="abs nl-title serif">Subscribe Our Newsletter</div>
<svg class="abs" style="left:440px;top:3018px" width="34" height="16"><path d="M1 8c8-6 16 6 30 0m-6-5l6 5-6 5" fill="none" stroke="#fff" stroke-width="1.5"/></svg>
<div class="abs nl-input">Enter Your Email Address</div>
<div class="abs nl-btn">Subscribe</div>

<!-- footer -->
<footer class="abs footer" role="img" aria-label="Dark city skyline background"></footer>
<div class="f-head" style="left:148px">Quick Links</div>
<ul class="abs f-links"><li>Home</li><li>About Us</li><li>Products</li><li>FAQ's</li><li>Contact Us</li></ul>

<div class="f-head" style="left:348px">Contact Details</div>
<div class="abs f-contact">
  <div><svg width="12" height="16" viewBox="0 0 12 16"><path d="M6 0a6 6 0 0 0-6 6c0 4.5 6 10 6 10s6-5.5 6-10a6 6 0 0 0-6-6z" fill="#fff"/><circle cx="6" cy="6" r="2.2" fill="#222"/></svg><span>Glintwell<br>0907 Lorem ipsum amet<br>co adipiscing dud</span></div>
  <div><svg width="14" height="14" viewBox="0 0 24 24"><path d="M5 2l4 0 2 5-2.5 2c1 2.5 3 4.5 5.5 5.5l2-2.5 5 2v4c-10 1-17-6-16-16z" fill="#fff"/></svg><span>123.456.7890</span></div>
  <div><svg width="14" height="14" viewBox="0 0 14 14"><rect x="1" y="5" width="12" height="6" fill="#fff"/><rect x="3" y="1" width="8" height="4" fill="#fff"/><rect x="3" y="9" width="8" height="4" fill="#fff" stroke="#222"/></svg><span>123.456.7890</span></div>
  <div><svg width="14" height="12" viewBox="0 0 14 12"><rect x="0.5" y="0.5" width="13" height="11" fill="none" stroke="#fff"/><path d="M1 1l6 5 6-5" fill="none" stroke="#fff"/></svg><span>info@glintwell.com</span></div>
</div>

<div class="f-head" style="left:597px">Quick Inquiry</div>
<div class="f-field" style="top:3137px">Name</div>
<div class="f-field" style="top:3167px">Email</div>
<div class="f-field" style="top:3197px;height:44px">Message</div>
<div class="btn f-submit">Submit</div>

<div class="abs f-logo serif">Glintwell</div>
<div class="social" style="left:914px"></div>
<div class="social" style="left:944px"></div>
<div class="social" style="left:974px"></div>
<div class="social" style="left:1004px"></div>

<div class="abs f-line"></div>
<div class="abs copy">Copyright © 2017 Glintwell. All Rights Reserved.</div>

</body>
</html>
```